Lustra Vale Label

Design a label for the new brand Lustra Vale. The specific product label : Lustra Vale Deep Moisturizing Conditioner.

You only need to design the front label.I have included the logo and a bottle jpeg. Please try your best.

Industry/Entity Type

Product

Requirements
Must have
• text you can use:
• For Dry, Damaged Hair
• Strengthening & Moisturizing Conditioner
• Moisture Infused
• Deep Penetrating Formula
• Used by Professionals
• 8.5oz/250ml

```html
<!DOCTYPE html>
<html lang="en">
<head>
<meta charset="utf-8">
<title>Lustra Vale Deep Moisturizing Conditioner – Front Label</title>
<link rel="stylesheet" href="https://fonts.googleapis.com/css2?family=Arimo:wght@700&display=swap">
<style>
  :root {
    --page: #efefef;
    --label-dark: #2b130a;
    --gold: #f8b400;
    --gold-light: #ffd84d;
    --gold-pale: #ffe98a;
    --ink-blue: #1c2bb5;
    --badge-red: #d8141b;
    --white: #ffffff;
  }
  html, body {
    margin: 0;
    padding: 0;
    width: 1200px;
    height: 3109px;
    overflow: hidden;
    background: var(--page);
  }
  .label {
    position: absolute;
    left: 40px;
    top: 280px;
    width: 1120px;
    height: 2780px;
    border-radius: 36px;
    overflow: hidden;
    background: var(--label-dark);
    font-family: "Arimo", Arial, sans-serif;
    font-weight: 700;
  }
  .label-art {
    position: absolute;
    inset: 0;
    width: 100%;
    height: 100%;
  }
  .badge {
    position: absolute;
    left: 250px;
    top: 520px;
    width: 380px;
    height: 210px;
    transform: rotate(-13deg);
    background: var(--badge-red);
    border-radius: 26px;
    box-shadow: 0 8px 0 rgba(0,0,0,0.25);
    text-align: center;
    line-height: 1;
  }
  .badge-new {
    display: block;
    color: var(--white);
    font-size: 96px;
    padding-top: 18px;
  }
  .badge-improved {
    display: block;
    color: var(--gold-light);
    font-size: 62px;
    margin-top: 6px;
  }
  .claim {
    position: absolute;
    left: 520px;
    top: 660px;
    width: 540px;
    color: var(--ink-blue);
    font-size: 64px;
    line-height: 1.1;
    text-align: center;
    white-space: nowrap;
    margin: 0;
  }
  .brand-name {
    position: absolute;
    left: 0;
    top: 1330px;
    width: 100%;
    text-align: center;
    color: var(--gold);
    font-size: 170px;
    line-height: 1;
    margin: 0;
  }
  .product-name {
    position: absolute;
    left: 0;
    top: 1950px;
    width: 100%;
    text-align: center;
    color: var(--ink-blue);
    font-size: 96px;
    line-height: 1.12;
    margin: 0;
  }
  .volume {
    position: absolute;
    left: 0;
    top: 2440px;
    width: 100%;
    text-align: center;
    color: var(--white);
    font-size: 66px;
    margin: 0;
  }
</style>
</head>
<body>
  <main class="label">
    <svg class="label-art" viewBox="0 0 1120 2780" preserveAspectRatio="none" aria-hidden="true">
      <defs>
        <linearGradient id="goldBand" x1="0" y1="0" x2="0" y2="1">
          <stop offset="0" stop-color="#ffd84d"/>
          <stop offset="0.5" stop-color="#ffe98a"/>
          <stop offset="1" stop-color="#f8b400"/>
        </linearGradient>
      </defs>
      <rect width="1120" height="2780" fill="#2b130a"/>
      <path d="M0,700 C380,720 740,420 1120,270 L1120,800 C920,1000 640,1140 0,1060 Z" fill="#f8b400"/>
      <path d="M0,740 C380,760 740,470 1120,330 L1120,760 C920,950 640,1090 0,1020 Z" fill="url(#goldBand)"/>
      <path d="M0,1900 C320,1800 760,1820 1120,1580 L1120,2320 C800,2330 380,2260 0,2420 Z" fill="#f8b400"/>
      <path d="M0,1940 C320,1850 760,1870 1120,1640 L1120,2280 C800,2290 380,2220 0,2370 Z" fill="url(#goldBand)"/>
    </svg>

    <div class="badge">
      <span class="badge-new">NEW</span>
      <span class="badge-improved">Improved</span>
    </div>

    <p class="claim">For Dry<br>Damaged Hair</p>

    <h1 class="brand-name">Lustra Vale</h1>

    <h2 class="product-name">Deep<br>Moisturizing<br>Conditioner.</h2>

    <p class="volume">8.5oz/250ml</p>
  </main>
</body>
</html>
```